Nice craft box with banderole or sticker

We want to get a packaging box design for the 3D puzzle. The packaging is craft paper print black or white, wrap with a banderole or wrap with a stikcer. This box should be designed in a minimalist style as much as possible, as shown in the attached file. Only the product photos are in color, and the colors of the box and packaging are relatively simple. The color of the banderole or adhesive should be suitable. Products of different colors can be placed on without conflict. If you have better ideas, it's also possible. our product name is 3D paper puzzle or 3D cardboard Model. it have animal puzzles, like birds, insect ,wild animal. it is for young chirdren. 5-12 years old. the design also can be similar as our file, but it should be better than it.

The box size is about : 12*19*1.2CM, Attach is some packing design ideal and our logo.
we like nice font for the text. and 1-3 nice icon.

We like more nice design. It can attract the eyes. We hope all items can be use same banderole, and just put different animal photo on it.

Also You can visit our website: www.velmaro.com. you can kow how about our product.

We attach 3 items photo. You can choose one to make the design. Our product is DIY, education. Animal with scene

Target Market(s)

Europe,Janpan,USA

Requirements
Must have
• Text is black for the craft box. nice color for the banderole or sticker.
Nice to have
• nice icon.
Should not have
• craft box should not be very colorful.

```html
<!DOCTYPE html>
<html lang="en">
<head>
<meta charset="UTF-8">
<title>3D Cardboard Puzzle – Animal 2 Box Front</title>
<link href="https://fonts.googleapis.com/css2?family=Poppins:wght@400;500;600;800&display=swap" rel="stylesheet">
<style>
  :root {
    --backdrop: #d8e6ed;
    --kraft: #cfa47c;
    --kraft-dark: #b9895f;
    --ink: #111111;
    --band-white: #ffffff;
    --band-blue: #1758a4;
    --title-blue: #1a56a0;
    --snail-light: #eee3cc;
    --snail-dark: #4a3a2c;
  }
  * { margin: 0; padding: 0; box-sizing: border-box; }
  html, body {
    width: 1161px; height: 1200px; overflow: hidden;
    background: var(--backdrop);
    font-family: "Poppins", sans-serif;
  }
  .box-front {
    position: absolute; left: 260px; top: 78px;
    width: 640px; height: 1043px;
    background: var(--kraft);
    color: var(--ink);
    overflow: hidden;
  }
  .mark-3d {
    position: absolute; top: 62px; left: 0; width: 100%;
    text-align: center; font-weight: 800; font-size: 142px; line-height: 1;
    letter-spacing: -6px;
  }
  .product-name {
    position: absolute; top: 205px; width: 100%; text-align: center;
    font-size: 36px; font-weight: 400;
  }
  .product-name strong { font-weight: 600; }
  .product-tagline {
    position: absolute; top: 259px; width: 100%; text-align: center;
    font-size: 20px; font-weight: 500;
  }
  .grid-patch {
    position: absolute; left: 506px; top: 29px; width: 110px; height: 107px;
    background: var(--kraft-dark);
  }
  .banderole {
    position: absolute; left: 0; top: 328px; width: 640px; height: 581px;
    background: var(--band-white);
  }
  .banderole-wave { position: absolute; left: 0; top: 0; }
  .brand {
    position: absolute; left: 40px; top: 22px; width: 64px;
    text-align: center; color: var(--title-blue);
  }
  .brand-dot {
    width: 54px; height: 54px; border-radius: 50%;
    background: var(--title-blue); margin: 0 auto 6px;
  }
  .brand-name { font-size: 16px; font-weight: 600; letter-spacing: 1px; }
  .series-title {
    position: absolute; right: 45px; top: 42px;
    font-size: 48px; font-weight: 500; color: var(--title-blue);
  }
  .product-photo {
    position: absolute; left: 96px; top: 184px; width: 368px; height: 288px;
    border-radius: 48% 52% 20% 20% / 60% 60% 20% 20%;
    background: linear-gradient(200deg, var(--snail-dark) 0%, #7b6450 45%, var(--snail-light) 85%);
  }
  .feature {
    position: absolute; top: 515px; display: flex; align-items: center; gap: 14px;
    color: #fff; font-size: 16px;
  }
  .feature-eco { left: 68px; }
  .feature-age { left: 338px; }
  .feature-icon {
    width: 54px; height: 54px; border-radius: 50%;
    border: 2px solid #fff; display: flex; align-items: center; justify-content: center;
  }
  .markets {
    position: absolute; right: 29px; top: 966px; font-size: 16px; font-weight: 500;
  }
</style>
</head>
<body>
  <main class="box-front">
    <div class="mark-3d">3D</div>
    <div class="product-name"><strong>Cardboard</strong> Puzzle</div>
    <div class="product-tagline">DIY Educational Animal Models</div>
    <div class="grid-patch" role="img" aria-label="Decorative grid pattern"></div>

    <section class="banderole">
      <svg class="banderole-wave" width="640" height="581" viewBox="0 0 640 581">
        <path d="M0 363 C 90 345 170 295 253 299 C 320 302 360 345 413 339 C 500 330 570 270 640 232 L640 581 L0 581 Z" fill="var(--band-blue)"/>
      </svg>
      <div class="brand">
        <div class="brand-dot"></div>
        <div class="brand-name">VELMARO</div>
      </div>
      <h1 class="series-title">Animal 2</h1>
      <div class="product-photo" role="img" aria-label="Assembled cardboard snail model with dark brown shell"></div>

      <div class="feature feature-eco">
        <span class="feature-icon">
          <svg width="26" height="26" viewBox="0 0 26 26" fill="none" stroke="#fff" stroke-width="2">
            <path d="M13 23 V12"/>
            <path d="M13 14 C 6 14 4 9 5 4 C 10 4 13 8 13 14 Z"/>
            <path d="M13 17 C 19 17 22 13 21 8 C 16 8 13 12 13 17 Z"/>
          </svg>
        </span>
        Eco-friendly materials
      </div>
      <div class="feature feature-age">
        <span class="feature-icon">
          <svg width="26" height="26" viewBox="0 0 26 26" fill="#fff">
            <circle cx="13" cy="8" r="5"/>
            <path d="M3 24 C 3 16 23 16 23 24 Z"/>
          </svg>
        </span>
        Suitable for ages 5–12
      </div>
    </section>

    <div class="markets">Europe | Japan | USA</div>
  </main>
</body>
</html>
```